Dubai Family protection infographic

We need to produce a way of attracting people to a life insurance and critical illness cover seminar. As this is a pretty dull subject for most people, so we need a cool way of getting people to read the invite/marketing collateral.

We're thinking some kind of colourful and attractive infographic that we can use on flyers and posters as well as online and as an emailer.

Content for the graphic is as bellow:

How much does it cost to replace Mum & Dad?

Mum = Chauffer, Cook, Laundry Service, Household Cleaner, Psychologist, Money Manager

Mums typically work a 94-hour week. At a rather paltry $12 per hour, that’s $4,888 per month – or $58,656 each year. (Source: wagelore.net)

Dad : The average Western Expat’s salary in the Gulf is $12,215 per month. That’s $146,580 each year. (Source: Palmcrest Ledger).

Did you know that the average age of critical illness claimants in the Middle East last year was just 48. Of these, 44% were for cancer while 41% were heart related.

The average age of a death claimant was just 50 years old.
(Source: Verenholt Assurance Group)

1 in 3 people will develop some form of cancer during their lifetime.

That’s 2.36 billion people globally.

And that’s equivalent to the population of China, USA, Brazil, Russia, Philippines, France, UK, South Africa and Italy combined.

Does your family have the resources to hand to cope if a tragedy happens to you?

What can you do to protect them and yourself?

Come to the UAE’s first national protection seminar to find out. Join us at Harbourline Riverside Sports Arena on June 19th at 19:00.

To pre-register, visit www.tovanmere.net/events or alternatively register on the door.

```html
<!DOCTYPE html>
<html lang="en">
<head>
<meta charset="utf-8">
<title>How much does it cost to replace Mum &amp; Dad?</title>
<link rel="stylesheet" href="https://fonts.googleapis.com/css2?family=Crimson+Pro:wght@700&display=swap">
<style>
  :root {
    --bg-light: #ffffff;
    --bg-edge: #dcdcdc;
    --yellow: #ffc414;
    --amber: #ffa000;
    --orange: #ff7a00;
    --red: #ff3a00;
    --deep-red: #e81c00;
    --frame: #ffffff;
    --rim: #ffe200;
    --ink: #ffffff;
  }
  * { margin: 0; padding: 0; box-sizing: border-box; }
  html, body { width: 863px; height: 1200px; overflow: hidden; }
  body {
    background: radial-gradient(ellipse 70% 60% at 50% 42%, var(--bg-light) 0%, #f6f6f6 55%, var(--bg-edge) 100%);
    font-family: "Crimson Pro", "Palatino Linotype", Georgia, serif;
    position: relative;
  }
  .card {
    position: absolute;
    border-radius: 48px;
  }
  .card--back-yellow {
    left: 86px; top: 196px; width: 650px; height: 610px;
    background: linear-gradient(135deg, var(--yellow), var(--orange));
    border: 5px solid var(--frame);
    transform: rotate(-9deg);
  }
  .card--back-red {
    left: 118px; top: 118px; width: 640px; height: 610px;
    background: linear-gradient(120deg, var(--orange), var(--deep-red));
    border: 5px solid var(--frame);
    transform: rotate(12deg);
  }
  .card--mid-orange {
    left: 96px; top: 168px; width: 650px; height: 610px;
    background: linear-gradient(135deg, var(--red), var(--orange) 60%, var(--amber));
    border: 5px solid var(--rim);
    box-shadow: 0 0 0 4px var(--frame);
    transform: rotate(-3deg);
  }
  .card--main {
    left: 92px; top: 150px; width: 655px; height: 600px;
    background:
      linear-gradient(160deg, rgba(255,255,255,0) 55%, rgba(255,255,255,0.18) 56%, rgba(255,255,255,0.1) 100%),
      linear-gradient(100deg, var(--amber) 0%, var(--orange) 35%, var(--red) 75%, var(--deep-red) 100%);
    border: 4px solid var(--frame);
    transform: rotate(7deg);
    box-shadow: 0 6px 18px rgba(0,0,0,0.15);
  }
  .invite {
    position: absolute;
    left: 60px; right: 60px; top: 34px;
    color: var(--ink);
    text-align: center;
    font-size: 12.6px;
    line-height: 16px;
  }
  .invite p { margin-bottom: 9px; }
  .invite__title {
    display: flex; align-items: center; justify-content: center; gap: 14px;
    font-size: 13.5px;
  }
  .invite__mark {
    width: 34px; height: 34px; border-radius: 50%;
    border: 2.5px solid var(--ink);
    flex: none;
  }
  .bubble {
    position: absolute;
    background: linear-gradient(135deg, var(--red), var(--orange) 70%, var(--amber));
    border: 4px solid var(--frame);
    border-radius: 14px;
  }
  .bubble--large { left: 628px; top: 790px; width: 118px; height: 118px; transform: rotate(-22deg); }
  .bubble--small { left: 742px; top: 915px; width: 64px; height: 64px; border-radius: 9px; transform: rotate(-22deg); }
  .shadow {
    position: absolute; border-radius: 50%;
    background: radial-gradient(ellipse, rgba(0,0,0,0.28), rgba(0,0,0,0) 70%);
  }
  .shadow--large { left: 590px; top: 918px; width: 150px; height: 22px; }
  .shadow--small { left: 740px; top: 986px; width: 110px; height: 16px; }
</style>
</head>
<body>
  <div class="card card--back-yellow"></div>
  <div class="card card--back-red"></div>
  <div class="card card--mid-orange"></div>
  <div class="card card--main">
    <div class="invite">
      <p class="invite__title"><span class="invite__mark"></span>How much does it cost to replace Mum &amp; Dad?</p>
      <p>Mum = Chauffer, Cook, Laundry Service, Household Cleaner, Psychologist, Money Manager</p>
      <p>Mums typically work a 94-hour week. At a rather paltry $12 per hour, that’s $4,888 per month<br>– or $58,656 each year. (Source: wagelore.net)</p>
      <p>Dad : The average Western Expat’s salary in the Gulf is $12,215 per month. That’s $146,580 each year.<br>(Source: Palmcrest Ledger).</p>
      <p>Did you know that the average age of critical illness claimants in the Middle East last year was just 48.<br>Of these, 44% were for cancer while 41% were heart related.</p>
      <p>The average age of a death claimant was just 50 years old.<br>(Source: Verenholt Assurance Group)</p>
      <p>1 in 3 people will develop some form of cancer during their lifetime.</p>
      <p>That’s 2.36 billion people globally.</p>
      <p>And that’s equivalent to the population of China, USA, Brazil, Russia, Philippines, France, UK,<br>South Africa and Italy combined.</p>
      <p>Does your family have the resources to hand to cope if a tragedy happens to you?</p>
      <p>What can you do to protect them and yourself?</p>
      <p>Come to the UAE’s first national protection seminar to find out. Join us at Harbourline Riverside<br>Sports Arena on June 19th at 19:00.</p>
      <p>To pre-register, visit www.tovanmere.net/events or alternatively register on the door.</p>
    </div>
  </div>
  <div class="shadow shadow--large"></div>
  <div class="bubble bubble--large"></div>
  <div class="shadow shadow--small"></div>
  <div class="bubble bubble--small"></div>
</body>
</html>
```